New travel store signage for Vellow Journeys to attract luxury travellers.

Hello,
We are looking to change the signage of our stores. The signage must include the following:
1. Vellow Journeys Logo (attached)
2. The text...The Travel & Cruise Experts
3. Brand Colours ( Fb0196, 412266, d41d84 and ffffff)
Please note the signage design must be central and only cover two thirds of the store front. We have also attached an image of one of our new stores which might be helpful when preparing a mock up.

We are looking for a quick turnaround on this, making a decision within 48 hours.

Target Market(s)

Retail

Industry/Entity Type

Travel Agency

Font styles to use
Other font styles liked:
• Radley

Colors
E54698
E96AAD
F1A4CE
F9D9EA
FCEFF6
6B429C
8869AF
B7A5CE
E3DAEB
F3F0F8

Requirements
Must have
• Hello, We are looking to change the signage of our stores. The signage must include the following: 1. Vellow Journeys Logo (attached) 2. The text...The Travel & Cruise Experts 3. Brand Colours ( Fb0196, 412266, d41d84 and ffffff) Please note the signage design must be central and only cover two thirds of the store front.
Should not have
• different colour or fonts. Gradient design.

```html
<!DOCTYPE html>
<html lang="en">
<head>
<meta charset="utf-8">
<title>Vellow Journeys – Store Signage</title>
<link rel="stylesheet" href="https://fonts.googleapis.com/css2?family=Radley&family=Roboto:wght@400;500&display=swap">
<style>
  :root {
    --brand-magenta: #d41d84;
    --brand-white: #ffffff;
    --canvas-bg: #efefef;
    --sign-shadow: rgba(0, 0, 0, 0.18);
  }

  * { margin: 0; padding: 0; box-sizing: border-box; }

  html, body {
    width: 898px;
    height: 1200px;
    overflow: hidden;
  }

  body {
    background: var(--canvas-bg);
    display: flex;
    align-items: center;
    justify-content: center;
  }

  .store-sign {
    position: relative;
    width: 840px;
    height: 196px;
    background: var(--brand-magenta);
    color: var(--brand-white);
    box-shadow: 0 6px 18px var(--sign-shadow);
    overflow: hidden;
  }

  .brand-name {
    position: absolute;
    left: 40px;
    top: 106px;
    display: flex;
    align-items: center;
    gap: 14px;
    font-family: "Radley", serif;
    font-size: 33px;
    line-height: 1;
    color: var(--brand-white);
  }

  .brand-dot {
    width: 22px;
    height: 22px;
    border-radius: 50%;
    background: var(--brand-white);
    flex-shrink: 0;
  }

  .tagline {
    position: absolute;
    right: 40px;
    top: 34px;
    font-family: "Roboto", sans-serif;
    font-weight: 500;
    font-size: 35px;
    line-height: 1;
    letter-spacing: 0.2px;
    text-align: right;
  }

  .web-address {
    position: absolute;
    right: 40px;
    top: 88px;
    font-family: "Roboto", sans-serif;
    font-weight: 400;
    font-size: 20px;
    line-height: 1;
    letter-spacing: 0.4px;
    text-align: right;
  }
</style>
</head>
<body>
  <section class="store-sign" aria-label="Vellow Journeys storefront sign">
    <div class="brand-name">
      <span class="brand-dot" aria-hidden="true"></span>
      <span>Vellow Journeys</span>
    </div>
    <p class="tagline">The Travel &amp; Cruise Experts</p>
    <p class="web-address">www.vellowjourneys.com</p>
  </section>
</body>
</html>
```